Wordpress Home Page

Management Consulting firm is seeking a creative wordpress designer to develop a home page our B to B website http://www.quorvanta.com. The owner is really looking for a home page that can tie in all the key subsections using recent post lists and sliders.

We run on wordpress with a wootheme. You can see our dev site to get a feel of the new colors we are using. http://dev.quorvanta.com

Industry/Entity Type

Management Consulting

Requirements
Must have
• Here are some features we are looking for:
* thematic sliders that represent our top sections for the site. Each slide would have 3 sections for the sub sections of the top section. We have a mockup

* A creative way to display most recent posts from the different subsections.

* Nice separation using graphics.

```html
<!DOCTYPE html>
<html lang="en">
<head>
<meta charset="utf-8">
<title>Quorvanta – Home</title>
<link rel="stylesheet" href="https://fonts.googleapis.com/css2?family=PT+Sans+Narrow:wght@400;700&family=PT+Sans:wght@400&family=Source+Code+Pro:wght@400&display=swap">
<style>
:root{
  --blue:#1ea5dd;
  --blue-dark:#1d3a6e;
  --orange:#f7901e;
  --green:#8dc63f;
  --nav:#3a3a3a;
  --ink:#3d3d3d;
  --body:#555;
  --muted:#f1f1f1;
  --rule:#dcdcdc;
}
*{margin:0;padding:0;box-sizing:border-box}
html,body{width:1200px;height:1166px;overflow:hidden}
body{position:relative;background:#fff;font-family:"PT Sans Narrow",sans-serif;color:var(--ink)}
.abs{position:absolute}
.topstrip{left:0;top:0;width:1200px;height:5px;background:#e4e4e4}
.brand{left:171px;top:17px;display:flex;align-items:center;gap:10px}
.brand-dot{width:55px;height:55px;border-radius:50%;background:#eee;border:2px solid #cfcfcf}
.brand-name{font-size:32px;letter-spacing:5px;line-height:1;color:#222}
.brand-sub{font-size:11px;color:#555;margin-top:3px;letter-spacing:.3px}
.hbtn{top:28px;height:33px;border:1px solid #e0e0e0;background:linear-gradient(#fff,#f2f2f2);font-size:14px;letter-spacing:1px;display:flex;align-items:center;justify-content:center}
.hbtn.reg{left:798px;width:116px;color:var(--orange)}
.hbtn.login{left:932px;width:97px;color:var(--blue)}
.nav{left:0;top:87px;width:1200px;height:37px;background:var(--nav)}
.nav ul{list-style:none;position:absolute;left:178px;width:849px;top:0;height:37px;display:flex;justify-content:space-between;align-items:center}
.nav li{color:#fff;font-size:14px;letter-spacing:1.2px}
.nav li.active{color:var(--blue)}
.feature{left:0;top:124px;width:1200px;height:418px;background:var(--muted)}
.card{top:137px;width:270px;height:297px;background:#fff;border:1px solid #e2e2e2;box-shadow:0 1px 3px rgba(0,0,0,.06);padding:14px}
.card-img{height:210px}
.card-cap{height:59px;background:var(--blue);color:#fff;padding:8px 12px;overflow:hidden}
.card-cap h3{font-size:15.5px;letter-spacing:1px;font-weight:700;line-height:19px}
.card-cap p{font-family:"Source Code Pro",monospace;font-size:8px;line-height:13px;margin-top:2px;white-space:nowrap}
.banner{left:171px;top:451px;width:858px;height:73px;background:linear-gradient(#fff,#f7f7f7);border:1px solid #e0e0e0;padding:13px 15px}
.banner h2{font-size:17px;letter-spacing:1px;font-weight:400;color:#3a3a3a}
.banner p{font-family:"PT Sans",sans-serif;font-size:9.5px;letter-spacing:.5px;margin-top:5px;color:#444}
.cta{left:844px;top:469px;width:170px;height:33px;border-radius:2px;background:linear-gradient(#fba640,#f28a14);border:1px solid #e07f10;color:#6b3200;font-size:15.5px;font-weight:700;letter-spacing:1px;display:flex;align-items:center;justify-content:center}
.sec-title{left:186px;top:568px;font-size:17px;font-weight:400;letter-spacing:1px;color:#333}
.rule{height:1px;background:var(--rule)}
.post{top:609px;height:274px;padding:6px 0 0 0}
.post+.post{border-left:1px solid var(--rule)}
.post-head{display:flex;gap:14px;height:92px}
.post-icon{width:34px;height:34px;border-radius:50%;flex:none;display:flex;align-items:center;justify-content:center}
.post h3{font-size:16.5px;line-height:24px;font-weight:400;letter-spacing:1px;color:#333;width:190px}
.post p{font-size:13px;line-height:22.3px;color:var(--body);margin-top:2px}
.more{font-size:13px;margin-top:8px;display:flex;align-items:center;gap:6px}
.more i{width:0;height:0;border-left:4px solid currentColor;border-top:3.5px solid transparent;border-bottom:3.5px solid transparent}
.photo{left:171px;top:928px;width:264px;height:137px;background:#fff;border:1px solid #e4e4e4;box-shadow:0 1px 3px rgba(0,0,0,.08);padding:8px}
.photo div{width:100%;height:100%;background:linear-gradient(135deg,#d8dde2,#9aa4ad 60%,#3c3f44)}
.lower h2{font-size:17px;letter-spacing:1px;font-weight:400;color:#333}
.lower p{font-size:13px;line-height:24px;color:var(--body);margin-top:11px}
.footer{left:0;top:1110px;width:1200px;height:56px;background:var(--blue);color:#fff;font-size:10px;letter-spacing:.8px}
.footer .copy{position:absolute;left:173px;top:21px}
.footer .copy b{font-weight:400;color:var(--blue-dark)}
.footer ul{position:absolute;right:171px;top:21px;list-style:none;display:flex;gap:14px}
.footer li.active{color:var(--blue-dark)}
</style>
</head>
<body>
<div class="abs topstrip"></div>

<header>
  <div class="abs brand">
    <div class="brand-dot"></div>
    <div>
      <div class="brand-name">Quorvanta</div>
      <div class="brand-sub">Performance Benchmarking</div>
    </div>
  </div>
  <div class="abs hbtn reg">Registered</div>
  <div class="abs hbtn login">Login</div>
</header>

<nav class="abs nav">
  <ul>
    <li class="active">HOME</li><li>ABOUT US</li><li>BENCHMARKING</li><li>SHOP</li><li>RESOURCE LIBRARY</li><li>CONTACT US</li>
  </ul>
</nav>

<section class="abs feature"></section>
<div class="abs card" style="left:171px">
  <div class="card-img" role="img" aria-label="Downloads box with green arrow illustration" style="background:linear-gradient(135deg,#eef1f2,#c9d2d6 60%,#9fc79a)"></div>
  <div class="card-cap"><h3>INSTANT DOWNLOADS</h3><p>Suspendisse scelerisque elit et feugiat grav<br>ida urna dui vulputate</p></div>
</div>
<div class="abs card" style="left:466px">
  <div class="card-img" role="img" aria-label="Printed sales charts and a pen" style="background:linear-gradient(135deg,#e9edf0,#cfd8df 50%,#e1a5a0)"></div>
  <div class="card-cap"><h3>DATA SALES</h3><p>Gerrlering scelerisque elit et feugiat grav<br>ida urna dui vulputate</p></div>
</div>
<div class="abs card" style="left:759px">
  <div class="card-img" role="img" aria-label="Illustration of a group of business people" style="background:linear-gradient(135deg,#c9c9c9,#8f8f8f 60%,#5a5a5a)"></div>
  <div class="card-cap"><h3>CUSTOM PEER GROUPS</h3><p>Suspendisse scelerisque elit et feugiat grav<br>ida urna dui vulputate onler</p></div>
</div>

<div class="abs banner">
  <h2>Benchmarking Solutions</h2>
  <p>With quorvanta benchmarking is now within the reach of virtually any organization or business.</p>
</div>
<div class="abs cta">Get Started</div>

<h2 class="abs sec-title">Latest Blog Posts</h2>
<div class="abs rule" style="left:171px;top:601px;width:858px"></div>

<article class="abs post" style="left:175px;width:277px;padding-right:10px">
  <div class="post-head">
    <div class="post-icon" style="background:var(--orange)"><svg width="20" height="14" viewBox="0 0 20 14" fill="#fff"><circle cx="5" cy="4" r="2.5"/><circle cx="15" cy="4" r="2.5"/><circle cx="10" cy="3.5" r="3"/><path d="M1 12c0-3 2-5 4-5s3 1 3 1 1-2 2-2 2 2 2 2 1-1 3-1 4 2 4 5z"/></svg></div>
    <h3>3 psychologically-based approaches to reducing call center turnover</h3>
  </div>
  <p>[This guest post was written by Dana Whitlow, an analyst for Ticketwise, as well as the managing editor for the Support Desk Review blog.] Many call center operators assume that turnover is just a fact of life. No amount of training or incentive will ever truly mitigate the trend, so why try? While retention will likely always [...]</p>
  <div class="more" style="color:var(--orange)">read more <i></i></div>
</article>

<article class="abs post" style="left:452px;width:288px;padding-left:12px;padding-right:6px">
  <div class="post-head">
    <div class="post-icon" style="background:var(--green)"><svg width="20" height="14" viewBox="0 0 20 14" fill="#fff"><circle cx="5" cy="4" r="2.5"/><circle cx="15" cy="4" r="2.5"/><circle cx="10" cy="3.5" r="3"/><path d="M1 12c0-3 2-5 4-5s3 1 3 1 1-2 2-2 2 2 2 2 1-1 3-1 4 2 4 5z"/></svg></div>
    <h3>Quorvanta announces appointment of new executive team</h3>
  </div>
  <p>Quorvanta, LLC, the leading provider of benchmarks for IT service and support professionals, has appointed a new executive team to lead the company. Effective immediately, Owen Prescott will assume all direct marketing and eCommerce responsibilities. Marisa Calder has been appointed to the position of Social Media and SEO Director. [...]</p>
  <div class="more" style="color:var(--green)">read more <i></i></div>
</article>

<article class="abs post" style="left:740px;width:289px;padding-left:11px">
  <div class="post-head">
    <div class="post-icon" style="background:var(--blue)"><svg width="20" height="14" viewBox="0 0 20 14" fill="#fff"><circle cx="5" cy="4" r="2.5"/><circle cx="15" cy="4" r="2.5"/><circle cx="10" cy="3.5" r="3"/><path d="M1 12c0-3 2-5 4-5s3 1 3 1 1-2 2-2 2 2 2 2 1-1 3-1 4 2 4 5z"/></svg></div>
    <h3>Video | service desk best practices</h3>
  </div>
  <p>Did you miss our Service Desk Best Practices webcast? For the first time ever, you can watch the full recording! Join the thousands of regular attendees who use Quorvanta’s monthly webcasts to achieve World-Class Performance. Here’s what some of our viewers have said: “Superb presentation, and marvelous set of tools discussed. [...]</p>
  <div class="more" style="color:var(--blue)">read more <i></i></div>
</article>

<div class="abs rule" style="left:171px;top:891px;width:858px"></div>

<div class="abs photo"><div role="img" aria-label="Business team meeting around a laptop"></div></div>
<section class="abs lower" style="left:465px;top:934px;width:564px">
  <h2>Lower Section Headline</h2>
  <p>Vestibulum non consectetur urna. Ut non quam quam. Nam congue rutrum leo, vel vulputate nibh mollis vel. Cras eleifend dui eget lectus vehicula eu ornare nunc sodales. Pellentesque habitant morbi tristique senectus et netus et malesuada fames ac turpis egestas. Cras luctus, turpis et semper rhoncus,</p>
  <div class="more" style="color:var(--blue);margin-top:11px">read more <i></i></div>
</section>

<footer class="abs footer">
  <div class="copy">Copyright © 2013 <b>business name</b> All rights reserved</div>
  <ul><li class="active">Home</li><li>About</li><li>Join</li><li>Blog</li><li>Contact</li></ul>
</footer>
</body>
</html>
```